Business Cards and Stationary for Physio
Brookvale Phsyiotherapy Clinic
Business Cards and Stationary for Physio -
Creative Brief
Simple
First Last
Physiotherapist B. Physio
Street Name, City, Zip
info@brookvalephysiotherapy.example
www.brookvalephysiotherapy.example
Brookvale Phsyiotherapy Clinic. Next Appointment Date Time

```html
<!DOCTYPE html>
<html lang="en">
<head>
<meta charset="utf-8">
<title>Brookvale Phsyiotherapy Clinic – Stationery</title>
<link rel="stylesheet" href="https://fonts.googleapis.com/css2?family=Lato:wght@400;700&display=swap">
<style>
:root{
  --bg:#e7e4df;
  --paper:#ffffff;
  --blue:#2b3d91;
  --green:#7cc142;
  --ink:#4a5568;
  --muted:#9aa3b2;
  --faint:#eef0f6;
  --shadow:0 2px 6px rgba(0,0,0,.12);
}
*{box-sizing:border-box;margin:0;padding:0}
html,body{width:1200px;height:730px;overflow:hidden;background:var(--bg);font-family:"Lato",sans-serif;color:var(--ink)}
.canvas{position:relative;width:1200px;height:730px}
.sheet{position:absolute;background:var(--paper);box-shadow:var(--shadow);overflow:hidden}
.card{width:250px;height:145px}
.swoosh{position:absolute;left:0;bottom:0;width:100%;display:block}
.brand{position:absolute;display:flex;align-items:center;gap:6px;color:var(--blue);font-weight:700;font-size:10px;letter-spacing:.02em;white-space:nowrap}
.brand-dot{width:9px;height:9px;border-radius:50%;background:var(--green);flex:none}
.person{position:absolute;right:16px;top:44px;text-align:left;font-size:9px;line-height:1.35}
.person .name{color:var(--blue);font-weight:700;font-size:10px}
.person .role{color:var(--green)}
.contact{position:absolute;left:16px;top:50px;font-size:7px;line-height:1.6;color:var(--ink);white-space:nowrap}
.appt-title{position:absolute;left:16px;top:40px;font-size:8px;font-weight:700;color:var(--green);letter-spacing:.06em}
.days{position:absolute;left:16px;top:56px;display:flex;gap:8px;font-size:7px}
.days span{display:flex;align-items:center;gap:3px}
.days span::before{content:"";width:7px;height:7px;border:1px solid var(--muted)}
.fields{position:absolute;left:16px;right:16px;top:78px;display:flex;gap:12px;font-size:7px}
.fields span{flex:1;border-bottom:1px solid var(--muted);padding-bottom:2px}
.appt-note{position:absolute;left:16px;bottom:14px;font-size:6px;color:var(--muted)}
.letter{width:270px;height:390px}
.faint-mark{position:absolute;left:50%;top:52%;width:130px;height:130px;margin:-65px 0 0 -65px;border-radius:50%;background:var(--faint)}
.lh-contact{position:absolute;right:18px;top:44px;font-size:6.5px;line-height:1.6;text-align:left;white-space:nowrap}
.lh-address{position:absolute;left:18px;bottom:62px;font-size:6.5px;line-height:1.6;white-space:nowrap}
.envelope{width:270px;height:140px}
.env-to{position:absolute;left:110px;top:64px;font-size:7px;line-height:1.7}
</style>
</head>
<body>
<main class="canvas">

  <section class="sheet card" style="left:40px;top:40px">
    <div class="brand" style="left:16px;top:16px"><span class="brand-dot"></span>Brookvale Phsyiotherapy Clinic</div>
    <div class="contact">Street Name, City, Zip<br>Tel 555 010 2040<br>info@brookvalephysiotherapy.example<br>www.brookvalephysiotherapy.example</div>
    <svg class="swoosh" viewBox="0 0 250 36" preserveAspectRatio="none" height="36"><path d="M0 36V22C70 4 150 2 250 12V36Z" fill="var(--green)"/><path d="M0 36V28C80 10 160 8 250 20V36Z" fill="var(--blue)"/></svg>
  </section>

  <section class="sheet card" style="left:305px;top:40px">
    <div class="brand" style="left:16px;top:16px"><span class="brand-dot"></span>Brookvale Phsyiotherapy Clinic</div>
    <div class="person"><div class="name">First Last</div><div class="role">Physiotherapist B. Physio</div></div>
    <svg class="swoosh" viewBox="0 0 250 36" preserveAspectRatio="none" height="36"><path d="M0 36V22C70 4 150 2 250 12V36Z" fill="var(--green)"/><path d="M0 36V28C80 10 160 8 250 20V36Z" fill="var(--blue)"/></svg>
  </section>

  <section class="sheet card" style="left:40px;top:200px">
    <div class="brand" style="left:16px;top:16px"><span class="brand-dot"></span>Brookvale Phsyiotherapy Clinic</div>
    <div class="appt-title">NEXT APPOINTMENT</div>
    <div class="days"><span>Mon</span><span>Tue</span><span>Wed</span><span>Thu</span><span>Fri</span><span>Sat</span></div>
    <div class="fields"><span>Date</span><span>Time</span></div>
    <div class="appt-note">Please give 24 hours notice if you cannot attend</div>
  </section>
  <section class="sheet card" style="left:305px;top:200px">
    <div class="brand" style="left:16px;top:16px"><span class="brand-dot"></span>Brookvale Phsyiotherapy Clinic</div>
    <div class="appt-title">NEXT APPOINTMENT</div>
    <div class="days"><span>Mon</span><span>Tue</span><span>Wed</span><span>Thu</span><span>Fri</span><span>Sat</span></div>
    <div class="fields"><span>Date</span><span>Time</span></div>
    <div class="appt-note">Please give 24 hours notice if you cannot attend</div>
  </section>

  <section class="sheet card" style="left:40px;top:360px">
    <div class="brand" style="left:16px;top:16px"><span class="brand-dot"></span>Brookvale Phsyiotherapy Clinic</div>
    <div class="contact">Street Name, City, Zip<br>Tel 555 010 2040<br>info@brookvalephysiotherapy.example<br>www.brookvalephysiotherapy.example</div>
    <svg class="swoosh" viewBox="0 0 250 36" preserveAspectRatio="none" height="36"><path d="M0 36V22C70 4 150 2 250 12V36Z" fill="var(--green)"/><path d="M0 36V28C80 10 160 8 250 20V36Z" fill="var(--blue)"/></svg>
  </section>
  <section class="sheet card" style="left:305px;top:360px">
    <div class="brand" style="left:16px;top:16px"><span class="brand-dot"></span>Brookvale Phsyiotherapy Clinic</div>
    <div class="person"><div class="name">First Last</div><div class="role">Physiotherapist B. Physio</div></div>
    <svg class="swoosh" viewBox="0 0 250 36" preserveAspectRatio="none" height="36"><path d="M0 36V22C70 4 150 2 250 12V36Z" fill="var(--green)"/><path d="M0 36V28C80 10 160 8 250 20V36Z" fill="var(--blue)"/></svg>
  </section>

  <section class="sheet card" style="left:40px;top:520px">
    <div class="brand" style="left:16px;top:16px"><span class="brand-dot"></span>Brookvale Phsyiotherapy Clinic</div>
    <div class="appt-title">NEXT APPOINTMENT</div>
    <div class="days"><span>Mon</span><span>Tue</span><span>Wed</span><span>Thu</span><span>Fri</span><span>Sat</span></div>
    <div class="fields"><span>Date</span><span>Time</span></div>
    <div class="appt-note">Please give 24 hours notice if you cannot attend</div>
  </section>
  <section class="sheet card" style="left:305px;top:520px">
    <div class="brand" style="left:16px;top:16px"><span class="brand-dot"></span>Brookvale Phsyiotherapy Clinic</div>
    <div class="appt-title">NEXT APPOINTMENT</div>
    <div class="days"><span>Mon</span><span>Tue</span><span>Wed</span><span>Thu</span><span>Fri</span><span>Sat</span></div>
    <div class="fields"><span>Date</span><span>Time</span></div>
    <div class="appt-note">Please give 24 hours notice if you cannot attend</div>
  </section>

  <section class="sheet letter" style="left:600px;top:30px">
    <div class="brand" style="left:18px;top:22px"><span class="brand-dot"></span>Brookvale Phsyiotherapy Clinic</div>
    <div class="faint-mark" role="img" aria-label="Faint clinic mark as background decoration"></div>
    <div class="lh-address">Street Name, City, Zip<br>Tel 555 010 2040<br>info@brookvalephysiotherapy.example<br>www.brookvalephysiotherapy.example</div>
    <svg class="swoosh" viewBox="0 0 270 44" preserveAspectRatio="none" height="44"><path d="M0 44V24C80 4 170 2 270 14V44Z" fill="var(--green)"/><path d="M0 44V32C90 12 180 10 270 24V44Z" fill="var(--blue)"/></svg>
  </section>

  <section class="sheet letter" style="left:900px;top:30px">
    <div class="brand" style="left:18px;top:22px"><span class="brand-dot"></span>Brookvale Phsyiotherapy Clinic</div>
    <div class="lh-contact">Street Name, City, Zip<br>Tel 555 010 2040<br>info@brookvalephysiotherapy.example</div>
    <div class="faint-mark" role="img" aria-label="Faint clinic mark as background decoration"></div>
  </section>

  <section class="sheet envelope" style="left:600px;top:460px">
    <div class="brand" style="left:16px;top:16px"><span class="brand-dot"></span>Brookvale Phsyiotherapy Clinic</div>
    <div class="contact" style="top:34px;font-size:6.5px">Street Name, City, Zip<br>www.brookvalephysiotherapy.example</div>
    <svg class="swoosh" viewBox="0 0 270 30" preserveAspectRatio="none" height="30"><path d="M0 30V16C80 2 170 0 270 8V30Z" fill="var(--green)"/><path d="M0 30V22C90 6 180 6 270 16V30Z" fill="var(--blue)"/></svg>
  </section>
  <section class="sheet envelope" style="left:900px;top:460px">
    <div class="brand" style="left:16px;top:16px"><span class="brand-dot"></span>Brookvale Phsyiotherapy Clinic</div>
    <div class="faint-mark" role="img" aria-label="Faint clinic mark as background decoration" style="left:auto;right:-10px;top:50%;width:90px;height:90px;margin:-45px 0 0 0"></div>
    <div class="env-to">First Last<br>Street Name<br>City, Zip</div>
  </section>

</main>
</body>
</html>
```